Zebra Romp - mobile play centre poster designs

Who are we - we are a mobile playground business that specialises in providing entertainment to children in a safe, clean environment either at home or in a function centre. Brief - create 4 different signs to be displayed on our playgrounds. Please find attached 3 photos from our competitors to use as a guide. Corflute sign - size A1 Toddler zone - size A1 Playground rules - size A4 No climbing - size 20cmx8cm sending through photos and documents now.
Colors
Designer to choose colors to be used in the design.
Requirements
Must have
- Colour, be very specific with the rules, pictures

```html
<!DOCTYPE html>
<html lang="en">
<head>
<meta charset="utf-8">
<title>Zebra Romp – No Climbing signs</title>
<link rel="stylesheet" href="https://fonts.googleapis.com/css2?family=Anton&family=Archivo+Black&display=swap">
<style>
  :root {
    --sign-red: #ec1c24;
    --ink: #000000;
    --paper: #ffffff;
    --fence-grey: #8a8a8a;
    --fence-light: #d4d4d4;
  }
  html, body {
    margin: 0;
    padding: 0;
    width: 1200px;
    height: 253px;
    overflow: hidden;
    background: var(--paper);
  }
  .sign-sheet {
    display: block;
    width: 1200px;
    height: 253px;
  }
  .frame-outer { fill: var(--sign-red); }
  .frame-inner { fill: var(--paper); }
  .word-no-block { font-family: "Archivo Black", "Arial Black", sans-serif; fill: var(--sign-red); }
  .word-no { font-family: "Anton", "Impact", sans-serif; fill: var(--sign-red); }
  .word-climbing { font-family: "Anton", "Impact", sans-serif; fill: var(--ink); }
  .brand-name { font-family: "Anton", "Impact", sans-serif; fill: var(--ink); letter-spacing: 1px; }
  .prohibit-line { stroke: var(--sign-red); stroke-linecap: butt; fill: none; }
</style>
</head>
<body>
<svg class="sign-sheet" viewBox="0 0 1200 253" xmlns="http://www.w3.org/2000/svg">
  <defs>
    <linearGradient id="fence-tone" x1="0" y1="0" x2="1" y2="1">
      <stop offset="0" stop-color="var(--fence-light)"/>
      <stop offset="1" stop-color="var(--fence-grey)"/>
    </linearGradient>
    <clipPath id="badge-clip">
      <circle cx="722" cy="93" r="55"/>
    </clipPath>
  </defs>

  <!-- Sign A: block heading -->
  <g class="sign sign-block">
    <rect class="frame-outer" x="0" y="0" width="571" height="228" rx="20"/>
    <rect class="frame-inner" x="20" y="20" width="532" height="188"/>

    <rect class="fence-climber" x="40" y="100" width="177" height="105" fill="url(#fence-tone)"
          role="img" aria-label="Pictogram of a person climbing a chain-link fence"/>
    <line class="prohibit-line" x1="64" y1="184" x2="193" y2="126" stroke-width="10"/>

    <text class="word-no-block" x="34" y="111" font-size="120" textLength="197" lengthAdjust="spacingAndGlyphs">NO</text>
    <text class="word-climbing" x="240" y="137" font-size="136" textLength="291" lengthAdjust="spacingAndGlyphs">CLIMBING</text>

    <text class="brand-name" x="300" y="190" font-size="30">ZEBRA ROMP</text>
  </g>

  <!-- Sign B: badge heading -->
  <g class="sign sign-badge">
    <rect class="frame-outer" x="629" y="0" width="571" height="228" rx="20"/>
    <rect class="frame-inner" x="649" y="20" width="532" height="188"/>

    <rect class="fence-climber" x="667" y="38" width="110" height="110" fill="url(#fence-tone)"
          clip-path="url(#badge-clip)"
          role="img" aria-label="Pictogram of a person climbing a chain-link fence"/>
    <circle class="prohibit-line" cx="722" cy="93" r="55" stroke-width="7"/>
    <line class="prohibit-line" x1="764" y1="56" x2="680" y2="130" stroke-width="6"/>

    <text class="word-no" x="787" y="133" font-size="121" textLength="77" lengthAdjust="spacingAndGlyphs">NO</text>
    <text class="word-climbing" x="883" y="133" font-size="121" textLength="284" lengthAdjust="spacingAndGlyphs">CLIMBING</text>

    <text class="brand-name" x="834" y="190" font-size="30">ZEBRA ROMP</text>
  </g>
</svg>
</body>
</html>
```